IT Company needs a flyer to present its new awesome app

We need a flayer that we will use for presenting an app called Otter Bell Bell to directors of companys for waste management. Great thing about our app is that it is multilingual and it has an alarm that will notify users when they need to prepare garbage for collection. Main colours are green and white and with this flayer we want to evoke a feeling of importance for being responsible citizen who knows how to manage with waste and how to recycle. App is available for Android and iOS. In the uploaded files there is an example of how we want it to look like (but much nicer :D) - we want big letters, bright colours, a little bit of pics and icons related to our subject and also a text part in which we will describe what this app does. There is also a logo of Otter Bell Bell.

```html
<!DOCTYPE html>
<html lang="hr">
<head>
<meta charset="utf-8">
<title>Otter Bell Bell – letak</title>
<link href="https://fonts.googleapis.com/css2?family=Anton&family=Mulish:wght@400;600;700;800&display=swap" rel="stylesheet">
<style>
  :root {
    --green: #6abd3f;
    --black: #000000;
    --white: #ffffff;
    --ink: #111111;
    --badge: #1c1c1c;
    --scene-light: #e9eff4;
    --scene-mid: #c9d8e6;
    --scene-low: #a8cf95;
    --screen-a: #f4f4f4;
    --screen-b: #dcdcdc;
  }
  * { margin: 0; padding: 0; box-sizing: border-box; }
  html, body { width: 855px; height: 1200px; overflow: hidden; background: var(--white); }
  .flyer {
    position: relative; width: 855px; height: 1200px; overflow: hidden;
    background: var(--white); font-family: "Mulish", sans-serif; color: var(--ink);
  }
  .corner-blob { position: absolute; top: 0; right: 0; }
  .brand-mark {
    position: absolute; left: 128px; top: 58px; width: 197px; text-align: center;
    font-weight: 800; color: var(--black); line-height: 1; letter-spacing: -0.5px;
  }
  .brand-mark .name-top { display: block; font-size: 52px; }
  .brand-mark .name-bottom { display: block; font-size: 32px; margin-top: 4px; }
  .headline { position: absolute; left: 68px; top: 188px; }
  .tagline {
    position: absolute; left: 70px; top: 430px;
    font-weight: 700; font-size: 24.5px; line-height: 30px; color: var(--ink);
  }
  .store-badge {
    position: absolute; top: 512px; height: 54px; border-radius: 6px;
    background: var(--badge); border: 1px solid #8a8a8a;
  }
  .store-badge.android { left: 69px; width: 167px; }
  .store-badge.ios { left: 251px; width: 186px; }
  .phone {
    position: absolute; left: 528px; top: 67px; width: 261px; height: 523px;
    border-radius: 36px; border: 7px solid var(--ink);
    background: linear-gradient(135deg, var(--screen-a) 0%, var(--screen-b) 45%, var(--screen-a) 70%, var(--white) 100%);
  }
  .phone .notch {
    position: absolute; top: -1px; left: 50%; transform: translateX(-50%);
    width: 108px; height: 16px; background: var(--ink); border-radius: 0 0 12px 12px;
  }
  .phone .screen-name {
    position: absolute; left: 0; right: 0; top: 206px;
    font-weight: 800; color: var(--black); text-align: center; line-height: 1; letter-spacing: -0.5px;
  }
  .phone .screen-name .name-top { display: block; font-size: 44px; }
  .phone .screen-name .name-bottom { display: block; font-size: 27px; margin-top: 4px; }
  .intro {
    position: absolute; left: 60px; top: 630px; width: 780px;
    font-size: 19.4px; line-height: 23.6px; font-weight: 400; white-space: nowrap;
  }
  .city-scene { position: absolute; left: 468px; top: 705px; }
  .feature { position: absolute; left: 66px; display: flex; align-items: flex-start; }
  .feature .icon {
    width: 86px; height: 86px; border-radius: 50%; background: var(--green);
    display: flex; align-items: center; justify-content: center; flex-shrink: 0;
  }
  .feature p {
    margin-left: 31px; font-size: 19.6px; line-height: 23.4px; white-space: nowrap;
  }
  .feature.schedule { top: 788px; }
  .feature.schedule p { margin-top: -8px; }
  .feature.growth { top: 903px; }
  .feature.growth p { margin-top: 3px; }
  .offer-band {
    position: absolute; left: 0; top: 1063px; width: 855px; height: 61px; background: var(--green);
    display: flex; align-items: center; padding-left: 69px;
    font-weight: 800; font-size: 20.5px; color: var(--ink);
  }
  .offer-band .link { font-weight: 700; font-size: 17.5px; margin-left: 12px; }
  .contact-band {
    position: absolute; left: 0; top: 1124px; width: 855px; height: 76px; background: var(--black);
    display: flex; align-items: center; padding-left: 69px;
    font-weight: 700; font-size: 24.5px; color: var(--white);
  }
  .contact-band .email { margin-left: 16px; }
</style>
</head>
<body>
<div class="flyer">
  <svg class="corner-blob" width="455" height="545" viewBox="0 0 455 545" aria-hidden="true">
    <path d="M0 0 H455 V545 C410 520 385 470 385 400 C385 300 360 230 300 205 C240 182 150 190 80 172 C25 158 0 110 0 55 Z" fill="var(--green)"/>
  </svg>

  <div class="brand-mark"><span class="name-top">otter</span><span class="name-bottom">bell bell</span></div>

  <svg class="headline" width="400" height="225" viewBox="0 0 400 225" aria-label="OTTER BELL BELL">
    <text x="0" y="126" textLength="398" lengthAdjust="spacingAndGlyphs"
          font-family="Anton, sans-serif" font-size="168" fill="var(--green)">OTTER</text>
    <text x="0" y="222" textLength="400" lengthAdjust="spacingAndGlyphs"
          font-family="Anton, sans-serif" font-size="112" fill="var(--black)">BELL BELL</text>
  </svg>

  <h2 class="tagline">Aplikacija koja za vas prati<br>raspored odvoza smeća</h2>

  <div class="store-badge android" role="img" aria-label="Gumb za preuzimanje aplikacije"></div>
  <div class="store-badge ios" role="img" aria-label="Drugi gumb za preuzimanje aplikacije"></div>

  <div class="phone">
    <span class="notch"></span>
    <div class="screen-name"><span class="name-top">otter</span><span class="name-bottom">bell bell</span></div>
  </div>

  <p class="intro">Otter Bell Bell je jednostavna aplikacija koja korisnike obavještava o odvozu<br>određene vrste otpada. Personalizirana je prema svakom davatelju usluge, a<br>glavno svojstvo joj je alarm koji korisnika dan prije ili na dan odvoza obavještava<br>da pripremi papir, plastiku, metal, staklo i ostale vrste otpada.</p>

  <svg class="city-scene" width="387" height="358" viewBox="0 0 387 358" role="img" aria-label="Ilustracija: komunalni radnici prazne kante u kamion za smeće ispred gradskih zgrada">
    <defs>
      <linearGradient id="sceneTone" x1="0" y1="0" x2="0" y2="1">
        <stop offset="0" stop-color="var(--scene-light)"/>
        <stop offset="0.6" stop-color="var(--scene-mid)"/>
        <stop offset="1" stop-color="var(--scene-low)"/>
      </linearGradient>
    </defs>
    <path d="M387 0 C350 20 320 45 280 45 C200 45 130 40 115 110 C105 160 125 210 80 225 C40 240 10 280 8 358 H387 Z" fill="url(#sceneTone)"/>
  </svg>

  <div class="feature schedule">
    <div class="icon">
      <svg width="46" height="46" viewBox="0 0 46 46" aria-hidden="true" fill="none" stroke="#fff" stroke-width="3">
        <rect x="3" y="8" width="40" height="34" rx="4"/>
        <line x1="3" y1="17" x2="43" y2="17"/>
        <line x1="13" y1="3" x2="13" y2="12"/><line x1="33" y1="3" x2="33" y2="12"/>
        <g fill="#fff" stroke="none">
          <rect x="9" y="22" width="7" height="4"/><rect x="20" y="22" width="7" height="4"/><rect x="31" y="22" width="7" height="4"/>
          <rect x="9" y="30" width="7" height="4"/><rect x="20" y="30" width="7" height="4"/><rect x="31" y="30" width="7" height="4"/>
        </g>
      </svg>
    </div>
    <p>Raspored odvoza smeća koji nam<br>pošaljete jednostavno ćemo<br>integrirati u aplikaciju i ona je<br>spremna za korištenje.</p>
  </div>

  <div class="feature growth">
    <div class="icon">
      <svg width="46" height="46" viewBox="0 0 46 46" aria-hidden="true" fill="#fff">
        <rect x="5" y="28" width="6" height="14"/><rect x="15" y="22" width="6" height="20"/>
        <rect x="25" y="26" width="6" height="16"/><rect x="35" y="16" width="6" height="26"/>
        <rect x="2" y="42" width="42" height="3"/>
        <polyline points="8,18 18,12 28,16 38,6" fill="none" stroke="#fff" stroke-width="3"/>
        <circle cx="8" cy="18" r="3"/><circle cx="18" cy="12" r="3"/><circle cx="28" cy="16" r="3"/><circle cx="38" cy="6" r="3"/>
      </svg>
    </div>
    <p>Unaprjedite svoje poslovanje i<br>povećajte zadovoljstvo svojih<br>korisnika uz Otter Bell Bell.</p>
  </div>

  <div class="offer-band">Ponudu možete zatražiti na linku: <span class="link">http://otterbell.example/Home/Pricing</span></div>
  <div class="contact-band">Za više informacija, javite nam se na: <span class="email">sales@otterbellbell.com</span></div>
</div>
</body>
</html>
```